Company Profile
Korvane Cargo Sdn Bhd is a well-established and experienced freight forwarder in Kuala Lumpur, Malaysia. We specialize in air and sea forwarding, Custom Brokerage and regulatory compliance services, inland transportation, overseas freighting and warehousing and distribution management. With our dedicated qualified and experienced professionals, we are fully committed to serving our clients.

Our Mission
Based on the motto “Quick, Reliable and Polite”, Korvane Cargo is dedicated to upholding the following three points corporate philosophy:1. Adhering to the principle that “the customer always comes first”.2. Contributing to the development of the local community.3. Making it our duty to be responsible and sincere.

Our Edge
• One-Stop Logistics Solutions
• Extensive Network Throughout Malaysia
• Highly Qualified and Experienced Pool of Professionals
• Comprehensive IT Solutions
• Innovative and Customer-focused Solutions
• Flexible and Consistent in Managing Exceptions
• Total Supply Chain Visibility

Target Market : We sell the logistics services to all the industry in Malaysia. (One Stop Logistics Solutions)

Business Card Detail : I would like to see the logo on the front with the general info.

Must Haves :
1) Name, Title, Office, Cell, Fax, Email, Address, Website
2) Must have complete company name show as : Korvane Cargo Sdn Bhd
3) Must have company registration no, show as : 8571620-W

Nice to Haves : Modern Design Business Card

Target Market(s)

We sell the logistics services to all the industry in Malaysia. (One Stop Logistics Solutions)

Contact Information for Business Card

I would like to see the logo on the front with the general info.

Colors

Designer to choose colors to be used in the design.

Requirements
Must have
• 1) Name, Title, Office, Cell, Fax, Email, Address, Website
• 2) Must have complete company name show as : Korvane Cargo Sdn Bhd
• 3) Must have company registration no, show as : 8571620-W
Nice to have
• Modern Design Business Card
Should not have
• Nil

```html
<!DOCTYPE html>
<html lang="en">
<head>
<meta charset="utf-8">
<title>Korvane Cargo Business Card</title>
<link href="https://fonts.googleapis.com/css2?family=Source+Sans+3:wght@400;600;700&display=swap" rel="stylesheet">
<style>
  :root {
    --navy: #0f4c8c;
    --sky: #2aa4e0;
    --ink: #4a4a4a;
    --paper: #ffffff;
    --stage: #2b2b2e;
  }
  * { margin: 0; padding: 0; box-sizing: border-box; }
  html, body { width: 1200px; height: 892px; overflow: hidden; }
  body {
    background: var(--stage);
    font-family: "Source Sans 3", "Segoe UI", sans-serif;
    position: relative;
  }
  .card {
    position: absolute;
    width: 600px;
    height: 343px;
    background: var(--paper);
    overflow: hidden;
    box-shadow: 0 10px 30px rgba(0,0,0,.45);
  }
  /* Front */
  .card-front { left: 80px; top: 70px; }
  .brand {
    position: absolute;
    left: 0; right: 0; top: 120px;
    display: flex;
    align-items: center;
    justify-content: center;
    gap: 22px;
  }
  .brand-dot {
    width: 58px; height: 58px;
    border: 3px solid var(--navy);
    border-radius: 50%;
  }
  .brand-rule { width: 2px; height: 70px; background: var(--navy); }
  .brand-name {
    font-weight: 700;
    font-size: 42px;
    letter-spacing: 3px;
    color: var(--navy);
    text-transform: uppercase;
  }
  .tagline {
    position: absolute;
    left: 0; right: 0; top: 232px;
    text-align: center;
    font-size: 17px;
    color: var(--ink);
  }
  /* Back */
  .card-back { left: 520px; top: 480px; }
  .back-band { position: absolute; inset: 0; }
  .back-name {
    position: absolute;
    right: 34px; top: 34px;
    font-weight: 700;
    font-size: 32px;
    letter-spacing: 2px;
    color: var(--navy);
    text-transform: uppercase;
  }
  .reg-no {
    position: absolute;
    right: 30px; top: 196px;
    font-size: 12px;
    color: var(--paper);
  }
  .holder { position: absolute; left: 34px; top: 92px; }
  .holder-name {
    font-weight: 700;
    font-size: 20px;
    color: var(--navy);
    text-transform: uppercase;
    line-height: 1;
  }
  .holder-title { font-size: 15px; color: var(--sky); margin-top: 2px; }
  .address {
    position: absolute;
    left: 34px; top: 146px;
    font-size: 12.5px;
    line-height: 15px;
    color: var(--ink);
    font-style: normal;
  }
  .contacts {
    position: absolute;
    left: 34px; top: 250px;
    list-style: none;
    color: var(--paper);
    font-size: 12.5px;
    line-height: 17px;
  }
  .contacts li { display: flex; align-items: center; gap: 10px; }
  .contacts svg { width: 11px; height: 11px; flex: none; }
</style>
</head>
<body>

<section class="card card-front">
  <div class="brand">
    <span class="brand-dot"></span>
    <span class="brand-rule"></span>
    <span class="brand-name">Korvane Cargo</span>
  </div>
  <p class="tagline">One Stop Logistics Specialist</p>
</section>

<section class="card card-back">
  <svg class="back-band" viewBox="0 0 600 343" preserveAspectRatio="none" aria-hidden="true">
    <path d="M0 238 L330 238 L410 150 L600 150 L600 343 L0 343 Z" fill="var(--navy)"/>
  </svg>
  <div class="back-name">Korvane Cargo</div>
  <div class="reg-no">Reg No: 8571620-W</div>

  <div class="holder">
    <div class="holder-name">Adrian Tan</div>
    <div class="holder-title">Managing Director</div>
  </div>

  <address class="address">
    Korvane Cargo Sdn Bhd<br>
    No.22B, 2nd Floor,<br>
    Jalan Seri Pantai 3B/KS4,<br>
    Taman Seri Pantai, 41150 Klang,<br>
    Selangor Darul Ehsan, Malaysia.
  </address>

  <ul class="contacts">
    <li><svg viewBox="0 0 12 12"><path d="M2 1 L4.5 1 L5 4 L3.6 5 Q4.8 7.4 7 8.4 L8 7 L11 7.5 L11 10 Q6 11.5 2.5 7 Q0.5 4 2 1 Z" fill="#fff"/></svg>(+603) 3102 5561 / 5562</li>
    <li><svg viewBox="0 0 12 12"><rect x="3" y="0.5" width="6" height="11" rx="1" fill="none" stroke="#fff" stroke-width="1.2"/><circle cx="6" cy="9.5" r=".7" fill="#fff"/></svg>(+6012) 457 2908</li>
    <li><svg viewBox="0 0 12 12"><rect x="3" y="1" width="6" height="4" fill="#fff"/><rect x="1" y="5" width="10" height="4.5" rx="1" fill="#fff"/><rect x="3" y="8" width="6" height="3" fill="#fff" stroke="var(--navy)" stroke-width=".6"/></svg>(+603) 3102 5563</li>
    <li><svg viewBox="0 0 12 12"><rect x="0.5" y="2" width="11" height="8" fill="#fff"/><path d="M0.5 2 L6 6.5 L11.5 2" fill="none" stroke="var(--navy)" stroke-width="1"/></svg>adrian.tan@korvanecargo.com.my</li>
    <li><svg viewBox="0 0 12 12"><circle cx="6" cy="6" r="5" fill="none" stroke="#fff" stroke-width="1.2"/><path d="M1 6 H11 M6 1 Q3 6 6 11 Q9 6 6 1" fill="none" stroke="#fff" stroke-width=".9"/></svg>www.korvanecargo.com.my</li>
  </ul>
</section>

</body>
</html>
```